Web Design Project - Tallow Analytics

I am a Mechanical Engineer running a one person consulting firm at this point. The hope is to expand in the future, but for now I simply need a website that conveys a professional appearance, and allows potential and existing clients to find me. Website design displaying contact information, CV for download, capabilities, past projects, etc. I've included four examples below from companies that provided the same service. I've only provided these as general reference for the type of work I do and how others have chosen to display this information. The design is completely at your discretion.

I've included the current Logo in the uploaded files section. I will provide content as requried.

http://www.quorvelmo.com/
http://www.truvane.com/
http://www.palqinsystems.com/
http://brindlowmechanics.net/

Industry/Entity Type

Consulting

```html
<!DOCTYPE html>
<html lang="en">
<head>
<meta charset="utf-8">
<title>Tallow Analytics – Engineering Consultants</title>
<link rel="stylesheet" href="https://fonts.googleapis.com/css2?family=Noto+Sans:wght@400;500;600&display=swap">
<style>
  :root {
    --orange: #ee7330;
    --orange-soft: #f6b48c;
    --grey-dark: #4b4b4d;
    --grey-mid: #8b8a8f;
    --grey-light: #d8d8d8;
    --text: #2b2b2b;
    --nav: #555458;
    --white: #ffffff;
  }
  * { box-sizing: border-box; margin: 0; padding: 0; }
  html, body { width: 1200px; height: 1024px; overflow: hidden; }
  body {
    font-family: "Noto Sans", Verdana, sans-serif;
    color: var(--text);
    background: var(--white);
    position: relative;
  }
  .site-header {
    height: 92px;
    background: radial-gradient(ellipse 420px 160px at 600px 20px, #ffffff 0%, #f3f3f3 45%, #bdbdbf 85%, #9c9c9f 100%);
    position: relative;
  }
  .brand {
    position: absolute; left: 170px; top: 22px;
    display: flex; align-items: center; gap: 10px;
  }
  .brand-mark { width: 22px; height: 22px; background: var(--orange); }
  .brand-name {
    font-size: 24px; font-weight: 600; color: var(--orange);
    letter-spacing: 0.5px;
  }
  .brand-sub {
    position: absolute; left: 170px; top: 62px;
    font-size: 9px; letter-spacing: 1px; color: var(--grey-dark);
  }
  .main-nav {
    position: absolute; right: 169px; top: 51px;
    display: flex; gap: 17px; font-size: 16px;
  }
  .main-nav a { color: var(--nav); text-decoration: none; }
  .main-nav a.is-current { color: var(--orange); }

  .hero {
    height: 347px;
    background: linear-gradient(90deg, var(--orange) 0%, var(--orange) 14%, #f7c6a6 30%, #fdfdfd 48%, #f3ece8 75%, var(--orange-soft) 86%, var(--orange) 100%);
    position: relative;
  }
  .hero-visual {
    position: absolute; left: 168px; top: 0; width: 870px; height: 347px;
    background:
      radial-gradient(ellipse 260px 200px at 52% 45%, rgba(220,230,244,0.9), rgba(255,255,255,0) 80%),
      linear-gradient(90deg, rgba(238,115,48,0.75) 0%, rgba(255,255,255,0.2) 30%, rgba(235,238,245,0.4) 70%, rgba(238,115,48,0.55) 100%);
  }

  .tagline {
    height: 49px;
    background: linear-gradient(90deg, #8e8d92, #a2a1a6 50%, #838287);
    display: flex; align-items: center; justify-content: center;
    font-size: 22px; color: #1f1f1f;
  }

  .projects {
    height: 389px;
    background: linear-gradient(180deg, #ffffff 0%, #ffffff 40%, #ececec 70%, #c9c9cb 100%);
  }
  .project-grid {
    width: 864px; margin: 0 auto;
    display: grid; grid-template-columns: repeat(4, 208px); column-gap: 10.6px;
  }
  .project-photo { height: 159px; }
  .project-photo.gears-silver { background: linear-gradient(135deg, #d9d9d9, #7c7c7e 50%, #bdbdbd); }
  .project-photo.gears-dark { background: radial-gradient(circle at 50% 40%, #b9b7c0, #2c2730 70%); }
  .project-photo.machine { background: linear-gradient(160deg, #a8a8a6, #4a4a4a 55%, #262626); }
  .project-photo.gears-blue { background: linear-gradient(135deg, #9fb6c8, #2f4e63 50%, #b8c9d4); }
  .project-title {
    margin-top: 7px; height: 29px;
    display: flex; align-items: center; justify-content: center;
    font-size: 16px; color: #2f2f2f;
    background: linear-gradient(90deg, #828187, #bdbcc0 50%, #d6d6d8);
  }
  .project-grid > article:nth-child(even) .project-title {
    background: linear-gradient(90deg, #c7c7ca, #a9a8ad 50%, #7b7a80);
  }
  .project-text {
    padding: 17px 12px 0 11px;
    font-size: 11.5px; line-height: 14px; text-align: justify;
  }

  .accent-bar { height: 15px; background: var(--orange); }
  .site-footer {
    height: 132px;
    background: radial-gradient(ellipse 420px 260px at 600px 130px, #9b9a9e 0%, #6f6e72 60%, var(--grey-dark) 100%);
    display: flex; justify-content: center; padding-top: 45px;
    font-size: 14px; color: var(--white);
  }
</style>
</head>
<body>
  <header class="site-header">
    <div class="brand">
      <span class="brand-mark"></span>
      <span class="brand-name">Tallow Analytics</span>
    </div>
    <div class="brand-sub">ENGINEERING CONSULTANTS</div>
    <nav class="main-nav">
      <a class="is-current" href="#">Home</a>
      <a href="#">About Tallow</a>
      <a href="#">Capabilities</a>
      <a href="#">Past Projects</a>
      <a href="#">CV</a>
      <a href="#">Contact</a>
    </nav>
  </header>

  <section class="hero">
    <div class="hero-visual" role="img" aria-label="Blueprint drawing of mechanical parts with a drafting compass and pencil"></div>
  </section>

  <div class="tagline">Place for some sort of slogan/tagline if you have one</div>

  <main class="projects">
    <div class="project-grid">
      <article class="project">
        <div class="project-photo gears-silver" role="img" aria-label="Interlocking silver gears"></div>
        <h2 class="project-title">Project 1</h2>
        <p class="project-text">Lorem ipsum dolor sit amet, consectetuer adipiscing elit, sed diam nonummy nibh euismod tincidunt ut laoreet dolore magna aliquam erat volutpat. Ut wisi enim ad minim veniam, quis nostrud exerci tation ullamcorper suscipit lobortis nisl ut aliquip ex ea commodo consequat.</p>
      </article>
      <article class="project">
        <div class="project-photo gears-dark" role="img" aria-label="Rows of machined metal gear hubs"></div>
        <h2 class="project-title">Project 2</h2>
        <p class="project-text">Lorem ipsum dolor sit amet, consectetuer adipiscing elit, sed diam nonummy nibh euismod tincidunt ut laoreet dolore magna aliquam erat volutpat. Ut wisi enim ad minim veniam, quis nostrud exerci tation ullamcorper suscipit lobortis nisl ut aliquip ex ea commodo consequat.</p>
      </article>
      <article class="project">
        <div class="project-photo machine" role="img" aria-label="Industrial machinery assembly"></div>
        <h2 class="project-title">Project 3</h2>
        <p class="project-text">Lorem ipsum dolor sit amet, consectetuer adipiscing elit, sed diam nonummy nibh euismod tincidunt ut laoreet dolore magna aliquam erat volutpat. Ut wisi enim ad minim veniam, quis nostrud exerci tation ullamcorper suscipit lobortis nisl ut aliquip ex ea commodo consequat.</p>
      </article>
      <article class="project">
        <div class="project-photo gears-blue" role="img" aria-label="Blue-tinted clockwork gears"></div>
        <h2 class="project-title">Project 4</h2>
        <p class="project-text">Lorem ipsum dolor sit amet, consectetuer adipiscing elit, sed diam nonummy nibh euismod tincidunt ut laoreet dolore magna aliquam erat volutpat. Ut wisi enim ad minim veniam, quis nostrud exerci tation ullamcorper suscipit lobortis nisl ut aliquip ex ea commodo consequat.</p>
      </article>
    </div>
  </main>

  <div class="accent-bar"></div>
  <footer class="site-footer">© Tallow Analytics 2013</footer>
</body>
</html>
```